Lease-A-Goose's web page

I need a web page(s) to show and promote my business of renting chickens. We provide seasonal rentals in the United States of a layer hen package for people who would like to try raising their own chickens. The package includes two hens, coop, attached run, feeder, waterer, and food. I would like interested people to be able to fill out a form so that I can have partners contact them to set up a delivery in their area. Our service is very popular with urban and suburban families.

Target Market(s)

Urban foodies.
Families.
People interested in Organic Foods.
People concerned with where their food comes from and how it is grown/prepared.
People interested in Urban Farming.

Industry/Entity Type

Business

Requirements
Must have
• A way for me to see rental interest based on zip code.
• A contact form including zip code, e-mail, and optional phone number.
• Our Logo. (Please contact if you are unable to use the file I provided.)
Nice to have
• A guest book for former renters that we can vet before posting.

```html
<!DOCTYPE html>
<html lang="en">
<head>
<meta charset="utf-8">
<title>Lease-A-Goose</title>
<link href="https://fonts.googleapis.com/css2?family=Open+Sans:ital,wght@0,300;0,400;0,600;0,700;1,400&family=Source+Sans+3:wght@400;600&display=swap" rel="stylesheet">
<style>
:root{
  --sky-top:#cdeefb;
  --sky:#d9f3fc;
  --blue:#2a8fd8;
  --title-blue:#1a6fb0;
  --grass:#6ccf1d;
  --grass-dark:#4fb012;
  --premium:#6cc644;
  --card-blue:#5bb7df;
  --text:#333;
  --muted:#777;
  --line:#e4e4e4;
  --panel:#ececec;
  --white:#fff;
}
*{box-sizing:border-box;margin:0;padding:0}
html,body{width:898px;height:1200px;overflow:hidden}
body{position:relative;font-family:"Open Sans",sans-serif;color:var(--text);
  background:linear-gradient(180deg,var(--sky-top) 0%,var(--sky) 100%)}
.abs{position:absolute}
.brand{left:374px;top:12px;width:150px;height:108px;display:flex;flex-direction:column;align-items:center;justify-content:center;gap:6px}
.brand-dot{width:60px;height:60px;border-radius:50%;background:var(--grass)}
.brand-name{font-weight:700;font-size:17px;color:var(--title-blue)}
.page{left:120px;top:130px;width:657px;height:960px;background:var(--white)}
.nav{left:120px;top:130px;width:657px;height:30px;background:var(--blue);display:flex;align-items:center;padding-left:10px}
.nav a{color:var(--white);text-decoration:none;font-size:11px;padding:0 13px;height:30px;line-height:30px}
.nav a.active{background:#4aaeea}
.social{position:absolute;right:10px;top:5px;display:flex;gap:8px}
.social span{width:20px;height:20px;border:1.5px solid #bfe3fa;border-radius:3px;display:block}
.hero-photo{left:120px;top:160px;width:445px;height:263px;
  background:linear-gradient(180deg,#5f8f3c 0%,#8fc155 45%,#6aa33a 100%)}
.hero-caption{left:120px;top:364px;width:445px;height:59px;background:rgba(0,0,0,.35);
  color:var(--white);font-weight:300;font-size:19px;line-height:18px;padding:10px 13px}
.hero-caption b{font-weight:700}
.form-panel{left:565px;top:160px;width:212px;height:263px;background:linear-gradient(160deg,#fff 0%,#f2fbe6 100%)}
.form-title{position:absolute;left:33px;top:10px;font-size:21px;color:var(--title-blue)}
.form-sub{position:absolute;left:33px;top:36px;font-size:9px;color:var(--muted)}
.field{position:absolute;left:32px;width:142px;height:15px;border:1px solid var(--line);background:var(--white);
  font-size:7px;color:#999;padding-left:7px;line-height:13px}
.submit{position:absolute;left:32px;top:215px;width:60px;height:18px;background:var(--grass-dark);color:var(--white);
  font-size:8px;font-weight:700;line-height:18px;text-align:center;border-radius:2px}
.band{left:120px;top:423px;width:657px;height:35px;background:var(--blue)}
.band-icon{position:absolute;left:16px;top:7px;width:22px;height:22px;border-radius:50%;background:var(--white)}
.band-title{position:absolute;left:47px;top:5px;color:var(--white);font-size:12px}
.band-sub{position:absolute;left:47px;top:19px;color:var(--white);font-size:9px}
.band-input{position:absolute;left:391px;top:9px;width:227px;height:19px;background:var(--white);font-size:7px;color:#aaa;padding:5px 14px}
.sec-title{font-size:14px;color:var(--text);line-height:14px}
.sec-sub{font-size:10px;font-style:italic;color:var(--text)}
.about{left:147px;top:486px;width:250px}
.about p{margin-top:6px;font-size:8.5px;line-height:11.5px;color:var(--muted)}
.testi{left:453px;top:486px;width:304px}
.testi-box{position:relative;margin-top:8px;height:87px;background:var(--panel);padding:20px 12px;font-size:7.5px;line-height:11.5px;color:#666}
.testi-name{position:absolute;right:22px;top:66px;font-size:8.5px;font-style:italic;font-weight:700;color:var(--text)}
.arrows{position:absolute;right:0;top:0;width:24px;height:11px;background:#d3d3d3;font-size:8px;color:#888;text-align:center;line-height:11px}
.packages-title{left:120px;top:657px;width:657px;text-align:center;font-family:"Source Sans 3",sans-serif;font-weight:600;font-size:23px}
.packages-text{left:160px;top:688px;width:577px;text-align:center;font-size:10.5px;line-height:12px;color:var(--muted)}
.card{border:3px solid var(--card-blue);background:var(--white);text-align:center}
.card .name{font-family:"Source Sans 3",sans-serif;font-weight:600;font-size:16px;color:var(--card-blue);padding-top:10px;line-height:20px}
.card .star{color:#ddd;font-size:10px;height:18px;border-bottom:1px solid var(--line);margin:0 8px}
.card .row{font-size:9px;color:#999;height:26px;line-height:26px;border-bottom:1px solid var(--line);margin:0 8px}
.card .foot{position:absolute;left:0;right:0;bottom:0;height:38px;background:#eee}
.btn{position:absolute;left:50%;transform:translateX(-50%);bottom:11px;width:56px;height:16px;border-radius:8px;
  background:var(--card-blue);color:var(--white);font-size:9px;font-weight:700;line-height:16px}
.card.std{position:absolute;width:121px;height:198px;top:772px}
.card.prem{position:absolute;left:379px;top:750px;width:147px;height:231px;border-color:var(--premium);box-shadow:0 2px 6px rgba(0,0,0,.15)}
.card.prem .name{color:var(--grass-dark);font-size:18px;padding-top:14px;line-height:22px}
.card.prem .row{height:30px;line-height:30px;font-size:10.5px}
.card.prem .foot{height:44px}
.card.prem .btn{background:var(--grass);width:64px;height:19px;line-height:19px;font-size:10px;bottom:12px}
.ribbon{position:absolute;left:-3px;top:-3px;width:44px;height:44px}
.trees{left:0;top:1052px;width:898px;height:60px;background:linear-gradient(180deg,rgba(108,207,29,0) 0%,#8fdc4a 45%,var(--grass) 100%)}
.ground{left:0;top:1110px;width:898px;height:90px;background:var(--grass)}
.foot-nav{left:0;top:1134px;width:898px;display:flex;justify-content:center;gap:27px;font-size:10.5px;color:#4a9a14}
.copy{left:0;top:1161px;width:898px;text-align:center;font-size:10.5px;color:var(--white)}
.copy span{color:#1f4a08}
</style>
</head>
<body>
  <div class="abs brand"><span class="brand-dot"></span><span class="brand-name">Lease-A-Goose</span></div>

  <div class="abs page"></div>

  <nav class="abs nav">
    <a class="active">HOME</a><a>PRICING</a><a>SERVICES</a><a>FAQ's</a><a>LEASE A GOOSE</a><a>ABOUT US</a><a>CONTACT US</a>
    <div class="social"><span></span><span></span><span></span></div>
  </nav>

  <div class="abs hero-photo" role="img" aria-label="Birds roaming a grassy orchard"></div>
  <div class="abs hero-caption">You can <b>rent</b> your chicken and<br>enjoy the benefits of owning a <b>chicken</b></div>

  <form class="abs form-panel">
    <div class="form-title">Lease a Goose!</div>
    <div class="form-sub">Fill out the form</div>
    <div class="field" style="top:75px">First Name</div>
    <div class="field" style="top:101px">Last Name</div>
    <div class="field" style="top:125px">Email</div>
    <div class="field" style="top:150px">Phone Number</div>
    <div class="field" style="top:176px">Zip Code</div>
    <div class="field" style="top:201px">Address</div>
    <div class="submit" style="top:229px">Submit</div>
  </form>

  <div class="abs band">
    <span class="band-icon"></span>
    <div class="band-title">Keep in touch with us</div>
    <div class="band-sub">Sign up now and you could recieve upto 25% discount on my chickens!</div>
    <div class="band-input">Enter email address</div>
  </div>

  <section class="abs about">
    <div class="sec-title">About Lease-A-Goose</div>
    <div class="sec-sub">Who we are and What we do</div>
    <p>Lorem ipsum dolor sit amet, consectetur adipiscing elit. Donec mattis consequat massa, a rhoncus nunc facilisis vel. Maecenas tristique orci dui. Cum sociis natoque penatibus et magnis dis parturient montes, nascetur ridiculus mus. Integer gravida egestas ante commodo mattis. Praesent ligula nisl, scelerisque et leo a, luctus vestibulum risus. Sed eu sapien vel dolor euismod porttitor lacinia sit amet arcu. Curabitur justo tellus, commodo vel nisl non.</p>
  </section>

  <section class="abs testi">
    <div class="sec-title">Clients Testimonials</div>
    <div class="sec-sub">What they say about our company</div>
    <div class="testi-box">
      <div class="arrows">‹ ›</div>
      Lorem ipsum dolor sit amet, consectetur adipiscing elit. Donec mattis consequat massa, a rhoncus nunc facilisis vel. Maecenas tristique orci dui. scelerisque et leo.A rhoncus nunc facilisis vel.
      <div class="testi-name">Dana Moore, Austin, Texas</div>
    </div>
  </section>

  <h2 class="abs packages-title">The Packages for Lease-A-Goose</h2>
  <p class="abs packages-text">Lorem ipsum dolor sit amet, consectetur adipiscing elit. Donec mattis consequat massa, a rhoncus nunc facilisis vel. Maecenas tristique orci dui. Cum sociis natoque penatibus et magnis<br>Dis parturient montes, nascetur ridiculus mus.</p>

  <div class="card std" style="left:260px">
    <div class="name">Standard</div><div class="star">★</div>
    <div class="row">One Hen</div><div class="row">Coop</div><div class="row">Attached Runner</div><div class="row" style="border:0">Feeder</div>
    <div class="foot"><div class="btn">RENT</div></div>
  </div>
  <div class="card std" style="left:525px">
    <div class="name">Standard</div><div class="star">★</div>
    <div class="row">One Hen</div><div class="row">Coop</div><div class="row">Attached Runner</div><div class="row" style="border:0">Feeder</div>
    <div class="foot"><div class="btn">RENT</div></div>
  </div>
  <div class="card prem">
    <svg class="ribbon" viewBox="0 0 44 44"><polygon points="0,28 28,0 44,0 0,44" fill="#4fb012"/><text x="18" y="20.5" text-anchor="middle" transform="rotate(-45 18 18)" font-family="Open Sans, sans-serif" font-size="7" font-weight="700" fill="#fff">$24.99</text></svg>
    <div class="name">Premium</div><div class="star">★</div>
    <div class="row">Two Hens</div><div class="row">Coop</div><div class="row">Attached Runner</div><div class="row" style="border:0">Feeder,Waterer &amp; Food</div>
    <div class="foot"><div class="btn">RENT</div></div>
  </div>

  <div class="abs trees" role="img" aria-label="Row of green trees along the horizon"></div>
  <div class="abs ground"></div>
  <nav class="abs foot-nav"><span>HOME</span><span>PRICING</span><span>SERVICES</span><span>FAQ's</span><span>LEASE A GOOSE</span><span>ABOUT US</span><span>CONTACT US</span></nav>
  <p class="abs copy"><span>Lease-A-Goose</span> Copyright 2013 | All rights reserved.</p>
</body>
</html>
```